Luftpolster-Versandtaschen  designen
Luftpolster-Versandtaschen designen
Zielgruppe
Es ist eine natürliche Schmerzsalbe entwickelt und hergestellt in Deutschland.
Die PELOR Salbe gibt ein zuverlässige Gefühl, durch ein innovatives Naturprodukt erstaunlich schnelle, wirkungsvolle Hilfe bei Schmerzen des Bewegungsapparates und bei Hautschäden zu erhalten und dabei gleichzeitig die Haut zu pflegen.
Aufgabenstellung
Wir möchten unsere Luftpolster-Versandtaschen gestalten lassen und das Corporate Design dort platzieren.
Ziel soll sein, das der Kunde eine hohe Aufmerksamkeit schon, vor dem Öffnen und das Vertrauen erhöht, schnelle Wiedererkennung der Marke Pelor Naturbalsam.
Die Druckdateien benötigen wir als pdf oder jedwede andere Datei mit einer Mindestauflösung von 300 dpi. Die Farbdarstellung erfolgt in CMYK. Alle Grafiken werden mittig platziert und proportional angepasst. Die genauen Maße der Versandtaschen bitte den Dokument vorlage_packbag entnehmen.
Farben / Texte / Bilder können von den Dokument (neue_webseite_alle_seiten_uebersicht) verwendet werden.
Bitte die Datei (vorlage_packbag_14d.pdf) von der Druckerei beachten.

```html
<!DOCTYPE html>
<html lang="de">
<head>
<meta charset="utf-8">
<title>Pelor Naturbalsam – Versandtasche</title>
<link href="https://fonts.googleapis.com/css2?family=Open+Sans:ital,wght@0,400;0,700;0,800;1,600;1,700&family=Arimo:wght@700&display=swap" rel="stylesheet">
<style>
  :root{
    --page:#ffffff;
    --bleed:#dadada;
    --frame:#2b3486;
    --edge:#1c2150;
    --orange-light:#f9b845;
    --orange-mid:#f6ad4a;
    --orange-deep:#ee7418;
    --icon:#f2ae55;
    --ink:#111111;
    --grey:#8a8a8a;
    --white:#ffffff;
  }
  html,body{margin:0;padding:0;width:1200px;height:1200px;overflow:hidden;background:var(--page);}
  .canvas{position:relative;width:1200px;height:1200px;font-family:"Open Sans",Arial,sans-serif;}

  .bag{position:absolute;left:433px;top:369px;width:333px;height:461px;background:var(--bleed);
       border-top:2px solid var(--edge);border-right:2px solid var(--edge);border-left:1px solid #b8b8b8;box-sizing:border-box;}
  .bag-label{position:absolute;left:0;width:100%;top:18px;text-align:center;padding-left:40px;box-sizing:border-box;
       font-family:"Arimo",Arial,sans-serif;font-weight:700;font-size:9px;color:var(--ink);}

  .print-area{position:absolute;left:452px;top:420px;width:295px;height:392px;background:var(--page);
       border:1.5px solid var(--frame);box-sizing:border-box;}

  .brand{position:absolute;left:553px;top:470px;width:74px;height:42px;display:flex;align-items:center;gap:5px;}
  .brand-dot{width:14px;height:14px;border-radius:50%;background:var(--orange-light);flex:none;}
  .brand-name{font-weight:800;font-size:9px;line-height:1.1;color:var(--ink);letter-spacing:.2px;}

  .hero{position:absolute;left:520px;top:527px;width:158px;height:153px;
       background:linear-gradient(90deg,var(--orange-mid) 0%,var(--orange-light) 20%,var(--orange-light) 80%,var(--orange-mid) 100%);}
  .hero-title{position:absolute;left:22px;top:46px;margin:0;font-weight:800;font-size:22px;line-height:19px;
       color:var(--orange-deep);letter-spacing:2.4px;}
  .hero-title .spread{letter-spacing:8.5px;}
  .hero-sub{position:absolute;left:22px;top:87px;margin:0;font-weight:800;font-size:13.5px;line-height:14px;color:var(--white);}

  .claim{position:absolute;left:452px;width:295px;top:686px;text-align:center;margin:0;
       font-style:italic;font-weight:600;font-size:8.3px;line-height:10.5px;color:var(--grey);letter-spacing:.6px;}

  .benefits{position:absolute;left:550px;top:716px;margin:0;padding:0;list-style:none;}
  .benefit{display:flex;align-items:center;height:17px;margin-bottom:8.5px;}
  .benefit-icon{width:17px;height:17px;flex:none;}
  .benefit-text{margin-left:3px;font-style:italic;font-weight:700;font-size:4.6px;color:var(--grey);letter-spacing:.2px;}
</style>
</head>
<body>
<div class="canvas">
  <div class="bag">
    <div class="bag-label">OBEN</div>
  </div>
  <div class="print-area"></div>

  <div class="brand">
    <span class="brand-dot"></span>
    <span class="brand-name">PELOR<br>NATURBALSAM</span>
  </div>

  <div class="hero">
    <h1 class="hero-title">ALWAYS<br><span class="spread">PELOR!</span></h1>
    <p class="hero-sub">MIT DER KRAFT<br>AUS DER NATUR</p>
  </div>

  <p class="claim">Hält jung, macht beweglich<br>Mit der 10-Kräuter-Aktivformel</p>

  <ul class="benefits">
    <li class="benefit">
      <svg class="benefit-icon" viewBox="0 0 20 20"><circle cx="10" cy="10" r="10" fill="var(--icon)"/>
        <path d="M10 15V9M10 10C8 10 6 9 6 6c3 0 4 1.5 4 4zM10 9c1-3 3-3.5 4.5-3.5 0 3-2 4-4.5 3.5z" fill="none" stroke="#fff" stroke-width=".9"/></svg>
      <span class="benefit-text">100% NATUR</span>
    </li>
    <li class="benefit">
      <svg class="benefit-icon" viewBox="0 0 20 20"><circle cx="10" cy="10" r="10" fill="var(--icon)"/>
        <path d="M5 10h10c0 3-2 5-5 5s-5-2-5-5zM11 10l3-5" fill="none" stroke="#fff" stroke-width=".9"/></svg>
      <span class="benefit-text">STÄRKT, PFLEGT, SCHÜTZT</span>
    </li>
    <li class="benefit">
      <svg class="benefit-icon" viewBox="0 0 20 20"><circle cx="10" cy="10" r="10" fill="var(--icon)"/>
        <path d="M10 4c-1.5 2-2.2 3.2-2.2 4.2a2.2 2.2 0 0 0 4.4 0C12.2 7.2 11.5 6 10 4zM5 13c2 0 3 1 5 1h4l-1 2H7" fill="none" stroke="#fff" stroke-width=".9"/></svg>
      <span class="benefit-text">ENTSPANNT UND REGENERIERT</span>
    </li>
  </ul>
</div>
</body>
</html>
```